Web Design for Financial Consulting Company

We need a website design for a financial consulting company "Kelvane Consulting". We build financial models, scenario analysis, handle the budgeting process and provide temporary staffing. I have over 10 years of experience. My Excel expertise and analytical savvy has saved clients over $17 million in profit.

Target Market(s)

Small to medium businesses

Industry/Entity Type

Financial Consulting

Number of Pages Required

4 page

Requirements
Must have
• Professional looking
Nice to have
• A little futuristic looking

```html
<!DOCTYPE html>
<html lang="en">
<head>
<meta charset="utf-8">
<title>Kelvane Consulting</title>
<link href="https://fonts.googleapis.com/css2?family=Poppins:wght@300;400;500;600;700&display=swap" rel="stylesheet">
<style>
:root{
  --blue:#00aeef;
  --navy:#0b3d6b;
  --ink:#1d2a3a;
  --text:#222;
  --grey-bg:#f4f4f4;
  --field:#ffffff;
  --muted:#8a8a8a;
}
*{box-sizing:border-box;margin:0;padding:0}
html,body{width:1200px;height:3507px;overflow:hidden;background:#fff}
body{font-family:'Poppins',sans-serif;color:var(--text)}
.page{position:relative;width:1200px;height:3507px;overflow:hidden}
.abs{position:absolute}

/* top bar */
.topbar{left:0;top:0;width:1200px;height:38px;background:var(--blue);color:#fff;font-size:14px}
.topbar .item{position:absolute;top:10px;display:flex;align-items:center;gap:8px}
.topbar svg{width:16px;height:16px}

/* header */
.header{left:0;top:38px;width:1200px;height:101px;background:#fff}
.brand{position:absolute;display:flex;align-items:center;gap:10px}
.brand .mark{width:34px;height:34px;border:4px solid var(--blue)}
.brand .name{font-weight:600;color:var(--navy);letter-spacing:2px;line-height:1.1}
.header .brand{left:84px;top:30px}
.header .brand .name{font-size:20px}
.nav{position:absolute;top:38px;font-size:15px;color:var(--ink);font-weight:400}
.nav.active{color:var(--blue)}
.nav.active::before{content:"";display:inline-block;width:7px;height:7px;background:var(--blue);margin-right:7px;vertical-align:middle}

/* hero */
.hero{left:0;top:139px;width:1200px;height:704px;background:linear-gradient(160deg,#ece9e4 0%,#d9cfc2 40%,#b89a7e 70%,#e6e2dc 100%)}
.hero-title{left:103px;top:232px;font-size:50px;line-height:57px;color:var(--navy);font-weight:300}
.hero-title strong{font-weight:600}
.dots{left:592px;top:740px;display:flex;gap:6px}
.dots span{width:14px;height:14px;border-radius:50%;background:var(--blue)}
.dots span:first-child{background:#fff}

/* section headings */
.sec-head{display:flex;align-items:center;gap:12px}
.sec-head .mark{width:42px;height:42px;border:4px solid var(--blue)}
.sec-head h2{font-size:30px;font-weight:600;color:var(--navy);line-height:1}
.sec-head .sub{font-size:15px;letter-spacing:6px;color:var(--blue);margin-top:4px}

/* about */
.about-photo{left:178px;top:948px;width:360px;height:267px;border-radius:8px;background:linear-gradient(135deg,#c9c2b8,#7f7868 55%,#3d3a35)}
.about-head{left:584px;top:985px}
.about-text{left:585px;top:1068px;width:470px;font-size:16px;line-height:31px;color:var(--text)}

/* services */
.services-head{left:489px;top:1380px}
.card{position:absolute;overflow:hidden}
.card .band{position:absolute;left:0;bottom:0;width:100%;background:rgba(20,20,20,.55);color:#fff;font-weight:600;font-size:20px;text-align:center;line-height:25px;display:flex;align-items:center;justify-content:center}
.card.featured .overlay{position:absolute;inset:0;background:rgba(14,74,130,.82);color:#fff;text-align:center;padding:0 28px;display:flex;flex-direction:column;justify-content:center}
.card.featured h3{font-size:20px;font-weight:600;line-height:25px;margin-bottom:14px}
.card.featured p{font-size:16px;line-height:26px}

/* contact */
.contact-bg{left:0;top:2309px;width:1200px;height:760px;background:var(--grey-bg)}
.contact-head{left:489px;top:2405px}
.field{position:absolute;background:var(--field);border:1px solid #e6e6e6;border-radius:8px;box-shadow:0 2px 4px rgba(0,0,0,.05);display:flex;align-items:center;gap:14px;padding-left:32px;font-size:17px;color:var(--muted)}
.field svg{width:16px;height:16px;fill:#9a9a9a}
.field.message{align-items:flex-start;padding-top:24px}
.submit{left:494px;top:2907px;width:218px;height:58px;border-radius:8px;background:var(--blue);color:#fff;font-size:16px;font-weight:500;display:flex;align-items:center;justify-content:center}

/* footer */
.footer{left:0;top:2990px;width:1200px;height:455px}
.footer-bg{left:0;top:3060px;width:1200px;height:385px;background:var(--navy)}
.footer .brand{left:122px;top:194px;flex-direction:column;gap:14px}
.footer .brand .mark{width:110px;height:110px;border:6px solid var(--blue)}
.footer .brand .name{font-size:30px;color:#fff;text-align:center}
.f-title{position:absolute;font-size:21px;color:var(--blue);font-weight:500}
.f-title::after{content:"";display:block;width:40px;height:2px;background:var(--blue);margin-top:8px}
.f-link{position:absolute;font-size:15px;color:#fff}
.f-link::before{content:"›";margin-right:10px;font-size:18px}
.f-row{position:absolute;display:flex;align-items:center;gap:14px;color:#fff;font-size:15px;line-height:18px}
.f-icon{width:32px;height:32px;border:1.5px solid #fff;border-radius:5px;display:flex;align-items:center;justify-content:center}
.f-icon svg{width:14px;height:14px;fill:#fff}
.copyright{left:0;top:3445px;width:1200px;height:62px;background:var(--blue);color:var(--navy);font-size:14px;display:flex;align-items:center;justify-content:center}
</style>
</head>
<body>
<div class="page">

  <div class="abs topbar">
    <div class="item" style="left:746px">
      <svg viewBox="0 0 16 16" fill="none" stroke="#fff" stroke-width="1.5"><path d="M4 2h3l1 4-2 1a8 8 0 0 0 3 3l1-2 4 1v3a2 2 0 0 1-2 2A11 11 0 0 1 2 4a2 2 0 0 1 2-2z"/></svg>
      <span>014-555-0192</span>
    </div>
    <div class="item" style="left:910px;font-size:13px">
      <svg viewBox="0 0 16 16" fill="none" stroke="#fff" stroke-width="1.5"><rect x="1" y="3" width="14" height="10"/><path d="M1 3l7 6 7-6"/></svg>
      <span>INFO@KELVANECONSULT.COM</span>
    </div>
  </div>

  <header class="abs header">
    <div class="brand"><span class="mark"></span><span class="name">KELVANE CONSULTING</span></div>
    <span class="nav active" style="left:706px">HOME</span>
    <span class="nav" style="left:801px">ABOUT US</span>
    <span class="nav" style="left:913px">SERVICES</span>
    <span class="nav" style="left:1019px">CONTACT US</span>
  </header>

  <section class="abs hero" role="img" aria-label="Photo of a finance team meeting in an office in front of a corkboard with sticky notes"></section>
  <svg class="abs" style="left:0;top:139px" width="1200" height="704" viewBox="0 0 1200 704">
    <path d="M0 704 L0 700 C200 600 430 600 620 660 C780 710 980 690 1200 580 L1200 704 Z" fill="#fff"/>
    <path d="M250 615 C420 590 520 620 620 660 C780 715 990 690 1200 575 L1200 555 C990 670 790 695 630 650 C520 610 420 585 250 615 Z" fill="#00aeef"/>
  </svg>
  <h1 class="abs hero-title">Helping your<br>finance team and<br><strong>Increasing Profit</strong></h1>
  <div class="abs dots"><span></span><span></span><span></span></div>

  <div class="abs about-photo" role="img" aria-label="Photo of a group of colleagues gathered around a laptop"></div>
  <div class="abs sec-head about-head">
    <span class="mark"></span>
    <div><h2>ABOUT US</h2><div class="sub">WHO WE ARE</div></div>
  </div>
  <p class="abs about-text">I am an experienced Finance professional who develops strategic financial plans, provides insightful analysis, and supports decision-making. With over 10 years of experience, I have successfully increased profitability for clients by $17M.</p>

  <div class="abs sec-head services-head">
    <span class="mark"></span>
    <div><h2>SERVICES</h2><div class="sub">WHAT WE DO</div></div>
  </div>

  <div class="card" role="img" aria-label="Photo of a woman working at a desk" style="left:87px;top:1514px;width:314px;height:379px;background:linear-gradient(160deg,#e8e6e2,#b8aa98 55%,#5e5346)">
    <div class="band" style="height:97px">FINANCIAL<br>MODELS – PROJECTS</div>
  </div>
  <div class="card featured" role="img" aria-label="Photo of hands reviewing documents" style="left:446px;top:1514px;width:314px;height:379px;background:linear-gradient(160deg,#7a8fa2,#3d4e5e)">
    <div class="overlay">
      <h3>BUDGETING<br>PROCESS</h3>
      <p>Building budgets from scratch, revamping current process to be more robust and scalable.</p>
    </div>
  </div>
  <div class="card" role="img" aria-label="Photo of three colleagues working at a round table" style="left:801px;top:1514px;width:315px;height:379px;background:linear-gradient(160deg,#f0efec,#c9c4bc 55%,#6b5f55)">
    <div class="band" style="height:90px;background:rgba(20,20,20,.35)">TEMPORARY<br>STAFFING</div>
  </div>
  <div class="card" role="img" aria-label="Photo of a laptop and camera on a wooden desk" style="left:87px;top:1933px;width:502px;height:291px;background:linear-gradient(150deg,#d8d6d2,#8a7868 50%,#3a3632)">
    <div class="band" style="height:98px">DATA CLEANSING</div>
  </div>
  <div class="card" role="img" aria-label="Photo of a man working at computer monitors" style="left:612px;top:1933px;width:502px;height:291px;background:linear-gradient(150deg,#e2e0dc,#9b9690 50%,#3a3836)">
    <div class="band" style="height:98px">PROCESS IMPROVEMENT</div>
  </div>

  <div class="abs contact-bg"></div>
  <div class="abs sec-head contact-head">
    <span class="mark"></span>
    <div><h2>CONTACT US</h2><div class="sub" style="letter-spacing:2px">HOW CAN WE HELP YOU</div></div>
  </div>

  <div class="field" style="left:173px;top:2551px;width:422px;height:65px">
    <svg viewBox="0 0 16 16"><circle cx="8" cy="5" r="3.2"/><path d="M2 15c0-4 3-6 6-6s6 2 6 6z"/></svg>First Name
  </div>
  <div class="field" style="left:605px;top:2551px;width:422px;height:65px">
    <svg viewBox="0 0 16 16"><path d="M1 3h14v10H1z M1 3l7 5 7-5" fill="#9a9a9a" stroke="#fff" stroke-width="1"/></svg>E-Mail
  </div>
  <div class="field" style="left:173px;top:2646px;width:422px;height:66px">
    <svg viewBox="0 0 16 16"><rect x="4" y="1" width="8" height="14" rx="1.5"/><rect x="5.5" y="3" width="5" height="9" fill="#fff"/></svg>Phone Number
  </div>
  <div class="field" style="left:605px;top:2646px;width:424px;height:66px">
    <svg viewBox="0 0 16 16"><path d="M8 1a5 5 0 0 0-5 5c0 4 5 9 5 9s5-5 5-9a5 5 0 0 0-5-5z"/><circle cx="8" cy="6" r="1.8" fill="#fff"/></svg>Address
  </div>
  <div class="field message" style="left:173px;top:2744px;width:856px;height:129px">
    <svg viewBox="0 0 16 16"><path d="M8 2C4 2 1 4.5 1 7.5c0 1.6.9 3 2.3 4L2.5 14l3-1.6c.8.2 1.6.3 2.5.3 4 0 7-2.5 7-5.5S12 2 8 2z"/></svg>Message
  </div>
  <div class="abs submit">SUBMIT NOW</div>

  <div class="abs footer-bg"></div>
  <div class="abs footer">
    <svg class="abs" style="left:0;top:0" width="1200" height="80" viewBox="0 0 1200 80">
      <path d="M0 70 C200 0 380 -5 560 40 C760 90 980 90 1200 10 L1200 80 L0 80 Z" fill="#00aeef"/>
      <path d="M0 80 C200 25 380 20 560 55 C760 100 980 95 1200 25 L1200 80 Z" fill="#0b3d6b"/>
    </svg>
    <div class="brand"><span class="mark"></span><span class="name">KELVANE<br>CONSULTING</span></div>

    <div class="f-title" style="left:427px;top:182px">Quick Links</div>
    <div class="f-link" style="left:433px;top:260px">Home</div>
    <div class="f-link" style="left:433px;top:290px">About Us</div>
    <div class="f-link" style="left:433px;top:321px">Services</div>
    <div class="f-link" style="left:433px;top:352px">Contact Us</div>

    <div class="f-title" style="left:619px;top:182px">Contact Us</div>
    <div class="f-row" style="left:619px;top:262px">
      <span class="f-icon"><svg viewBox="0 0 16 16"><path d="M4 2h3l1 4-2 1a8 8 0 0 0 3 3l1-2 4 1v3a2 2 0 0 1-2 2A11 11 0 0 1 2 4a2 2 0 0 1 2-2z"/></svg></span>
      <span>CALL US<br>8014 555 0193</span>
    </div>
    <div class="f-row" style="left:619px;top:318px">
      <span class="f-icon"><svg viewBox="0 0 16 16"><path d="M1 4h14v9H1z"/></svg></span>
      <span>EMAIL US<br>info@kelvaneconsult.com</span>
    </div>
    <div class="f-row" style="left:619px;top:374px">
      <span class="f-icon"><svg viewBox="0 0 16 16"><path d="M8 1a5 5 0 0 0-5 5c0 4 5 9 5 9s5-5 5-9a5 5 0 0 0-5-5z"/></svg></span>
      <span>Address line Dummy Here<br>Address line Here</span>
    </div>

    <div class="f-title" style="left:913px;top:182px">Follow Us</div>
    <div class="f-row" style="left:916px;top:262px"><span class="f-icon"></span><span>LINKORA</span></div>
    <div class="f-row" style="left:916px;top:315px"><span class="f-icon"></span><span>CHIRPNET</span></div>
    <div class="f-row" style="left:916px;top:367px"><span class="f-icon"></span><span>SNAPFRAME</span></div>
  </div>

  <div class="abs copyright">Copyright © 2023 All Rights Reserved By Company name</div>
</div>
</body>
</html>
```